Marlow crest Letter head

Need a heeder and footer for 8.5 x 11 paper
2 inch top header, 1.5 inch bottom footer
Add logo, agent pictures, names and titles (Broker), office picture with address
Marlow Crest Real Estate
20387 Route 512
Seabrook Point, SC 29990
Please make phone # large (555) 304-7182
MarlowCrestRealEstate.example

```html
<!DOCTYPE html>
<html lang="en">
<head>
<meta charset="utf-8">
<title>Marlow Crest Real Estate — Letterhead</title>
<link rel="stylesheet" href="https://fonts.googleapis.com/css2?family=Open+Sans:wght@400;600;700&family=Roboto:wght@400;500&family=Roboto+Slab:wght@400;600&display=swap">
<style>
  :root {
    --backdrop: #e9e6e1;
    --paper: #ffffff;
    --paper-shade: #f1f1f1;
    --ink: #3c3c3c;
    --ink-soft: #4a4a4a;
    --brand-red: #c1272d;
    --brand-navy: #27306b;
    --photo-left: #d9a48c;
    --photo-left-top: #e6cfa2;
    --photo-right: #2b3446;
    --photo-right-top: #b9aaa0;
    --signature: #e4e4e4;
  }
  * { box-sizing: border-box; margin: 0; padding: 0; }
  html, body {
    width: 1084px; height: 1200px; overflow: hidden;
    background: var(--backdrop);
  }
  .letterhead {
    position: absolute; left: 92px; top: 17px;
    width: 900px; height: 1165px;
    background: linear-gradient(180deg, var(--paper) 0%, var(--paper-shade) 22%, var(--paper) 38%, var(--paper) 55%, var(--paper-shade) 78%, var(--paper) 80%, var(--paper-shade) 100%);
    box-shadow: 0 2px 10px rgba(0,0,0,.18);
    font-family: "Open Sans", Arial, sans-serif;
    color: var(--ink);
  }
  .brand {
    position: absolute; left: 85px; top: 116px;
    display: flex; align-items: center; gap: 10px;
  }
  .brand-mark { width: 16px; height: 16px; background: var(--brand-red); flex: none; }
  .brand-name {
    font-family: "Open Sans", Arial, sans-serif;
    font-weight: 700; font-size: 20px; color: var(--brand-navy);
    letter-spacing: .2px; white-space: nowrap;
  }
  .contact {
    position: absolute; left: 531px; top: 80px;
    font-family: "Roboto", Arial, sans-serif; font-style: normal;
    font-size: 15.5px; line-height: 20px; color: #333;
    white-space: nowrap;
  }
  .contact-line { display: flex; align-items: center; gap: 6px; }
  .contact-line svg { width: 13px; height: 13px; fill: var(--brand-red); flex: none; }
  .contact-phone { font-weight: 500; }
  .letter-body {
    position: absolute; left: 80px; top: 280px; width: 738px;
    font-size: 15.2px; line-height: 22.6px; color: var(--ink-soft);
    letter-spacing: -0.15px;
  }
  .salutation { margin-bottom: 24px; }
  .letter-body p.paragraph { text-align: justify; hyphens: auto; margin-bottom: 23px; }
  .closing { margin-top: 2px; }
  .signature {
    position: absolute; left: 84px; top: 880px; width: 72px; height: 86px;
    background: var(--signature); border-radius: 6px;
  }
  .agent-photo { position: absolute; top: 1015px; width: 141px; height: 150px; }
  .agent-photo--left {
    left: 0;
    background: linear-gradient(180deg, var(--photo-left-top) 0%, var(--photo-left) 55%, #e2475e 75%, #e2475e 100%);
  }
  .agent-photo--right {
    right: 0;
    background: linear-gradient(180deg, var(--photo-right-top) 0%, #a89086 45%, var(--photo-right) 68%, var(--photo-right) 100%);
  }
  .agent-name {
    position: absolute; top: 1122px;
    font-family: "Roboto Slab", Georgia, serif; font-size: 15.5px;
    display: flex; align-items: center; gap: 5px; white-space: nowrap;
  }
  .agent-name--left { left: 169px; }
  .agent-name--right { right: 157px; }
  .agent-full { color: var(--brand-red); font-weight: 600; }
  .agent-title { color: var(--brand-navy); font-size: 13.5px; }
  .agent-dot { width: 4px; height: 4px; background: var(--brand-navy); border-radius: 50%; }
</style>
</head>
<body>
  <main class="letterhead">
    <header>
      <div class="brand">
        <span class="brand-mark"></span>
        <span class="brand-name">Marlow Crest Real Estate</span>
      </div>
      <address class="contact">
        <div>20387 Route 512</div>
        <div>Seabrook Point, SC 29990</div>
        <div class="contact-line contact-phone">
          <svg viewBox="0 0 24 24"><path d="M6.6 10.8a15.1 15.1 0 0 0 6.6 6.6l2.2-2.2a1 1 0 0 1 1-.25 11.4 11.4 0 0 0 3.6.57 1 1 0 0 1 1 1V20a1 1 0 0 1-1 1A17 17 0 0 1 3 4a1 1 0 0 1 1-1h3.5a1 1 0 0 1 1 1c0 1.25.2 2.45.57 3.57a1 1 0 0 1-.25 1z"/></svg>
          (555) 304-7182
        </div>
        <div class="contact-line">
          <svg viewBox="0 0 24 24"><path d="M2 5h20v2l-10 6L2 7zM2 9l10 6 10-6v10H2z"/></svg>
          info@MarlowCrestRealEstate.example
        </div>
        <div class="contact-line">
          <svg viewBox="0 0 24 24"><path d="M12 2a10 10 0 1 0 0 20 10 10 0 0 0 0-20zm6.9 6h-3a15.7 15.7 0 0 0-1.4-3.6A8 8 0 0 1 18.9 8zM12 4a14 14 0 0 1 1.9 4h-3.8A14 14 0 0 1 12 4zM4.3 14a8.2 8.2 0 0 1 0-4h3.4a16.5 16.5 0 0 0 0 4zm.8 2h3a15.7 15.7 0 0 0 1.4 3.6A8 8 0 0 1 5.1 16zm3-8h-3a8 8 0 0 1 4.4-3.6A15.7 15.7 0 0 0 8.1 8zM12 20a14 14 0 0 1-1.9-4h3.8A14 14 0 0 1 12 20zm2.3-6H9.7a14.7 14.7 0 0 1 0-4h4.6a14.7 14.7 0 0 1 0 4zm.2 5.6a15.7 15.7 0 0 0 1.4-3.6h3a8 8 0 0 1-4.4 3.6zm1.8-5.6a16.5 16.5 0 0 0 0-4h3.4a8.2 8.2 0 0 1 0 4z"/></svg>
          MarlowCrestRealEstate.example
        </div>
      </address>
    </header>

    <section class="letter-body" lang="en">
      <p class="salutation">Dear customer,</p>
      <p class="paragraph">Lorem ipsum dolor sit amet, consectetur adipisicing elit, sed do eiusmod tempor incididunt ut labore et dolore magna aliqua. Ut enim ad minim veniam, quis nostrud exercitation ullamco laboris nisi ut aliquip ex ea commodo consequat. Duis aute irure dolor in reprehenderit in voluptate velit esse cillum dolore eu fugiat nulla pariatur. Excepteur sint occaecat cupidatat non proident, sunt in culpa qui officia deserunt mollit anim id est laborum.</p>
      <p class="paragraph">Lorem ipsum dolor sit amet, consectetur adipisicing elit, sed do eiusmod tempor incididunt ut labore et dolore magna aliqua. Ut enim ad minim veniam, quis nostrud exercitation ullamco laboris nisi ut aliquip ex ea commodo consequat. Duis aute irure dolor in reprehenderit in voluptate velit esse cillum dolore eu fugiat nulla pariatur. Excepteur sint occaecat cupidatat non proident, sunt in culpa qui officia deserunt mollit anim id est laborum.</p>
      <p class="paragraph">Lorem ipsum dolor sit amet, consectetur adipisicing elit, sed do eiusmod tempor incididunt ut labore et dolore magna aliqua. Ut enim ad minim veniam, quis nostrud exercitation ullamco laboris nisi ut aliquip ex ea commodo consequat. Duis aute irure dolor in reprehenderit in voluptate velit esse cillum dolore eu fugiat nulla pariatur. Excepteur sint occaecat cupidatat non proident, sunt in culpa qui officia deserunt mollit anim id est laborum.</p>
      <p class="paragraph">Lorem ipsum dolor sit amet, consectetur adipisicing elit, sed do eiusmod tempor incididunt ut labore et dolore magna aliqua. Ut enim ad minim veniam, quis nostrud exercitation ullamco laboris nisi ut aliquip ex ea commodo consequat. Duis aute irure dolor in reprehenderit.</p>
      <p class="closing">Yours Sincerely,</p>
    </section>

    <div class="signature" role="img" aria-label="Handwritten signature"></div>

    <footer>
      <div class="agent-photo agent-photo--left" role="img" aria-label="Portrait photo of broker Dana Whitlock"></div>
      <div class="agent-name agent-name--left">
        <span class="agent-full">Dana Whitlock</span><span class="agent-dot"></span><span class="agent-title">Broker</span>
      </div>
      <div class="agent-name agent-name--right">
        <span class="agent-title">Broker</span><span class="agent-dot"></span><span class="agent-full">Glen Whitlock</span>
      </div>
      <div class="agent-photo agent-photo--right" role="img" aria-label="Portrait photo of broker Glen Whitlock"></div>
    </footer>
  </main>
</body>
</html>
```